Wealth Education Business Needs Sharp Business Card Design

We need a business card design for a recently launched investor education business called Harbor Ledger.

The final design should promote security, empowerment, self improvement and financial gain. The card will ideally promote the stature of the business.

For more information and colours please visit harborledger-example.com.au

Target Market(s)

Corporate executives and high net worth individuals

Industry/Entity Type

Education

Contact Information for Business Card

Name
Position
Contact Address
Phone
Mobile
Email
Website

```html
<!DOCTYPE html>
<html lang="en">
<head>
<meta charset="UTF-8">
<title>Harbor Ledger – Business Card</title>
<link href="https://fonts.googleapis.com/css2?family=Lato:wght@400;700&display=swap" rel="stylesheet">
<style>
  :root{
    --backdrop:#e9e9e9;
    --card-white:#ffffff;
    --ink:#2b2b2b;
    --wordmark-grey:#3d3d3d;
    --teal:#128a8c;
    --teal-deep:#06686a;
    --teal-light:#0e9595;
    --white:#ffffff;
  }
  *{margin:0;padding:0;box-sizing:border-box;}
  html,body{width:1200px;height:720px;overflow:hidden;}
  body{background:var(--backdrop);font-family:"Lato",Arial,sans-serif;position:relative;}

  .card{position:absolute;top:240px;width:420px;height:240px;border-radius:14px;}
  .card-front{left:148px;background:var(--card-white);color:var(--ink);}
  .card-back{left:633px;background:linear-gradient(135deg,var(--teal-light) 0%,var(--teal) 45%,var(--teal-deep) 100%);}

  .wordmark{position:absolute;left:0;right:0;text-align:center;font-weight:400;text-transform:uppercase;white-space:nowrap;}
  .card-front .wordmark{top:34px;font-size:33px;letter-spacing:4px;color:var(--wordmark-grey);}
  .card-back .wordmark{top:100px;font-size:33px;letter-spacing:4px;color:var(--white);}

  .holder{position:absolute;right:24px;top:110px;text-align:right;}
  .holder-name{font-size:16px;font-weight:700;color:var(--teal);line-height:1.2;}
  .holder-role{font-size:11.5px;color:var(--ink);margin-top:2px;}

  .contact-list{position:absolute;left:16px;top:168px;list-style:none;font-size:12.5px;line-height:14.5px;}
  .contact-list li{display:flex;align-items:center;gap:5px;}
  .icon{width:11px;height:11px;fill:var(--teal-deep);flex:none;}

  .address{position:absolute;right:16px;top:187px;font-size:12.5px;line-height:14.5px;text-align:right;}
  .address-line{display:flex;align-items:center;justify-content:flex-end;gap:4px;}
  .address-line.second{padding-right:16px;}
</style>
</head>
<body>
  <section class="card card-front" aria-label="Business card front">
    <div class="wordmark">Harbor Ledger</div>

    <div class="holder">
      <div class="holder-name">Marcus Bell</div>
      <div class="holder-role">Director</div>
    </div>

    <ul class="contact-list">
      <li>
        <svg class="icon" viewBox="0 0 12 12"><path d="M1 4c0-1.2 1-2 3-2h4c2 0 3 .8 3 2v1H8.5V4h-5v1H1z M3 6h6l1.5 4.5h-9z"/></svg>
        1300 555 014
      </li>
      <li>
        <svg class="icon" viewBox="0 0 12 12"><path d="M3.5 0.5h5a1 1 0 0 1 1 1v9a1 1 0 0 1-1 1h-5a1 1 0 0 1-1-1v-9a1 1 0 0 1 1-1zM4 2v7h4V2z"/></svg>
        +613 5550 1290
      </li>
      <li>
        <svg class="icon" viewBox="0 0 12 12"><path d="M0.5 2h11v8h-11z" /><path d="M1 2.5l5 4 5-4" stroke="#fff" stroke-width="1" fill="none"/></svg>
        support@harborledger-example.com.au
      </li>
      <li>
        <svg class="icon" viewBox="0 0 12 12"><circle cx="6" cy="6" r="5.5"/><path d="M0.5 6h11M6 0.5v11M6 0.5c-3 3-3 8 0 11M6 0.5c3 3 3 8 0 11" stroke="#fff" stroke-width="0.8" fill="none"/></svg>
        www.harborledger-example.com.au
      </li>
    </ul>

    <div class="address">
      <div class="address-line">
        Level 3, 42 Quayside Lane
        <svg class="icon" viewBox="0 0 12 12"><path d="M6 1l5.5 5H10v5H7.5V8h-3v3H2V6H0.5z"/></svg>
      </div>
      <div class="address-line second">Melbourne VIC 3000</div>
    </div>
  </section>

  <section class="card card-back" aria-label="Business card back">
    <div class="wordmark">Harbor Ledger</div>
  </section>
</body>
</html>
```